Business Card Design

Hoping for a black background business card, minimalistic design.
With the Copper Lantern logo you created in white.

I would like to include:
My Name and title
Address (street address)
Reception: (phone number)
Fax: (fax number)
Reception: (email address)
Direct email: (email address)
Instagram: (ig handle)

```html
<!DOCTYPE html>
<html lang="en">
<head>
<meta charset="utf-8">
<title>Copper Lantern — Business Card</title>
<link rel="stylesheet" href="https://fonts.googleapis.com/css2?family=Lato:wght@300;400;700;900&display=swap">
<style>
  :root {
    --backdrop: #2b2c2f;
    --card-dark: #1c1c1d;
    --card-light: #ffffff;
    --ink: #111111;
    --ink-soft: #555555;
    --ring: #ececec;
    --paper-white: #ffffff;
  }
  * { box-sizing: border-box; margin: 0; padding: 0; }
  html, body {
    width: 1200px; height: 952px; overflow: hidden;
    background: var(--backdrop);
    font-family: "Lato", sans-serif;
  }
  .stage {
    position: relative; width: 1200px; height: 952px;
    display: flex; flex-direction: column; align-items: center; justify-content: center; gap: 56px;
  }
  .card {
    position: relative; width: 560px; height: 320px;
    border-radius: 26px; overflow: hidden;
    box-shadow: 0 18px 40px rgba(0,0,0,0.45);
  }

  /* Back of card */
  .card--back { background: var(--card-dark); color: var(--paper-white); }
  .brand-lockup {
    position: absolute; left: 78px; top: 112px;
    display: flex; align-items: center; gap: 20px;
  }
  .brand-lockup__dot {
    width: 64px; height: 64px; border-radius: 50%;
    border: 3px solid var(--paper-white); flex: none;
  }
  .brand-lockup__rule { width: 1.5px; height: 104px; background: var(--paper-white); flex: none; }
  .brand-lockup__name {
    font-weight: 400; font-size: 34px; letter-spacing: 2px; text-transform: uppercase; line-height: 1;
  }
  .brand-lockup__services { font-weight: 300; font-size: 13.5px; margin-top: 8px; letter-spacing: 0.3px; }

  /* Front of card */
  .card--front { background: var(--card-light); color: var(--ink); }
  .person { position: absolute; left: 40px; top: 30px; }
  .person__name { font-size: 22px; font-weight: 400; letter-spacing: 0.5px; text-transform: uppercase; }
  .person__name strong { font-weight: 900; }
  .person__title { font-size: 16px; font-weight: 300; color: var(--ink-soft); margin-top: 2px; }
  .person__rule { width: 50px; height: 2px; background: var(--ink); margin-top: 8px; }

  .contact-list { position: absolute; left: 40px; top: 116px; list-style: none; }
  .contact-list li {
    display: flex; align-items: flex-start; gap: 9px;
    font-size: 12px; color: var(--ink-soft); line-height: 1.35; margin-bottom: 4px;
  }
  .contact-list .label { font-weight: 700; color: var(--ink); }
  .contact-list svg { width: 14px; height: 14px; flex: none; margin-top: 1px; }

  .emblem {
    position: absolute; right: 28px; bottom: -70px;
    width: 228px; height: 228px; border-radius: 50%;
    border: 11px solid var(--ring);
    display: flex; align-items: center; justify-content: center;
  }
  .emblem__name {
    font-weight: 900; font-size: 22px; letter-spacing: 1px; text-transform: uppercase;
    color: var(--ink); margin-top: -60px; text-align: center; line-height: 1.1;
  }
</style>
</head>
<body>
<main class="stage">

  <section class="card card--back" aria-label="Card back">
    <div class="brand-lockup">
      <span class="brand-lockup__dot"></span>
      <span class="brand-lockup__rule"></span>
      <div>
        <div class="brand-lockup__name">Copper Lantern</div>
        <div class="brand-lockup__services">Chiropractic | Physiotherapy Massage Therapy</div>
      </div>
    </div>
  </section>

  <section class="card card--front" aria-label="Card front">
    <div class="person">
      <h1 class="person__name">Daniel R. <strong>Whitmore</strong></h1>
      <p class="person__title">Managing Director</p>
      <div class="person__rule"></div>
    </div>

    <ul class="contact-list">
      <li>
        <svg viewBox="0 0 14 14"><rect width="14" height="14" rx="2" fill="#111"/><path d="M7 3a2.6 2.6 0 0 0-2.6 2.6C4.4 7.6 7 11 7 11s2.6-3.4 2.6-5.4A2.6 2.6 0 0 0 7 3z" fill="#fff"/><circle cx="7" cy="5.6" r="1" fill="#111"/></svg>
        <span>1372 Harbor View Lane<br>Portland, OR 97205</span>
      </li>
      <li>
        <svg viewBox="0 0 14 14"><rect width="14" height="14" rx="2" fill="#111"/><path d="M4.5 3.2l1.6-.2.8 2-1 .8a5.5 5.5 0 0 0 2.3 2.3l.8-1 2 .8-.2 1.6c-3.6.3-6.6-2.7-6.3-6.3z" fill="#fff"/></svg>
        <span><span class="label">Reception:</span> +00 987 654 32</span>
      </li>
      <li>
        <svg viewBox="0 0 14 14"><rect width="14" height="14" rx="2" fill="#111"/><rect x="3.5" y="6" width="7" height="4.5" fill="none" stroke="#fff" stroke-width="1.1"/><rect x="5" y="3.2" width="4" height="2.8" fill="none" stroke="#fff" stroke-width="1"/></svg>
        <span><span class="label">Fax:</span> +00 987 654 33</span>
      </li>
      <li>
        <svg viewBox="0 0 14 14"><rect width="14" height="14" rx="2" fill="#111"/><rect x="3" y="4.2" width="8" height="5.6" fill="none" stroke="#fff" stroke-width="1.1"/><path d="M3 4.2l4 3 4-3" fill="none" stroke="#fff" stroke-width="1.1"/></svg>
        <span><span class="label">Reception:</span> hello@copperlantern.com</span>
      </li>
      <li>
        <svg viewBox="0 0 14 14"><rect width="14" height="14" rx="2" fill="#111"/><rect x="3" y="4.2" width="8" height="5.6" fill="none" stroke="#fff" stroke-width="1.1"/><path d="M3 4.2l4 3 4-3" fill="none" stroke="#fff" stroke-width="1.1"/></svg>
        <span><span class="label">Direct:</span> daniel@copperlantern.com</span>
      </li>
      <li>
        <svg viewBox="0 0 14 14"><rect width="14" height="14" rx="2" fill="#111"/><circle cx="7" cy="7" r="2" fill="none" stroke="#fff" stroke-width="1.1"/><path d="M9 7v.8a1.3 1.3 0 0 0 2.6 0V7A4.6 4.6 0 1 0 9.5 10.8" fill="none" stroke="#fff" stroke-width="1"/></svg>
        <span><span class="label">Instagram:</span> @copperlanternclinic</span>
      </li>
      <li>
        <svg viewBox="0 0 14 14"><rect width="14" height="14" rx="2" fill="#111"/><circle cx="7" cy="7" r="3.8" fill="none" stroke="#fff" stroke-width="1.1"/><path d="M3.2 7h7.6M7 3.2c-1.6 2.2-1.6 5.4 0 7.6M7 3.2c1.6 2.2 1.6 5.4 0 7.6" fill="none" stroke="#fff" stroke-width="0.9"/></svg>
        <span>www.copperlantern.com</span>
      </li>
    </ul>

    <div class="emblem">
      <span class="emblem__name">Copper<br>Lantern</span>
    </div>
  </section>

</main>
</body>
</html>
```